IT company needs A4 Cover page design for our sales proposals

We need a A4 cover page designed for use with our Brightquill Offer (Venmarq) quoting software. This cover page will be used for PDF and print.

We are a Managed IT Service Provider serving small to medium sized businesses based in the UK.

The design needs to convey professionalism, technology and people

Must incorporate the new Banner Ad theme we have just had designed through this website (PixelMeadow project number 5842096 https://www.pixelmeadow.co.uk/project-progress/overview.aspx?briefId=5842096)

It is recommended to be 1240 x 1754

Target Market(s)

Small to medium sized companies - verticals include Healthcare, Accounting, Engineering, Manufacturing

Industry/Entity Type

It Company

Colors
f37122
000000
b7b7b7
eaeaea

Requirements
Must have
• Must incorporate our logo, strap line and picture of the person as per PixelMeadow project 5842096 https://www.pixelmeadow.co.uk/project-progress/overview.aspx?briefId=5842096
• Must convey business, professionalism, technology and people
• Must have a picture of a person using technlogy
• Use our corporate colours of orange, black, grey & white as per www.quillbarrow.co.uk

```html
<!DOCTYPE html>
<html lang="en">
<head>
<meta charset="utf-8">
<title>Quillbarrow – Quote Cover</title>
<link rel="stylesheet" href="https://fonts.googleapis.com/css2?family=Didact+Gothic&family=Montserrat:wght@600;800&display=swap">
<style>
  :root {
    --orange: #f37122;
    --orange-band: #f5823d;
    --black: #111111;
    --grey-light: #eaeaea;
    --grey-panel: #c8c9cb;
    --white: #ffffff;
    --blue-deep: #1ea7df;
    --blue-soft: #bfe0f2;
  }
  html, body {
    margin: 0;
    padding: 0;
    overflow: hidden;
    background: var(--white);
  }
  .cover {
    position: relative;
    width: 849px;
    height: 1200px;
    overflow: hidden;
    background: var(--white);
  }
  .cover-shapes {
    position: absolute;
    inset: 0;
  }
  .brand {
    position: absolute;
    left: 57px;
    top: 150px;
    display: flex;
    align-items: center;
    gap: 14px;
  }
  .brand-dot {
    width: 30px;
    height: 30px;
    border-radius: 50%;
    background: var(--orange);
  }
  .brand-name {
    font-family: "Montserrat", sans-serif;
    font-weight: 800;
    font-size: 38px;
    letter-spacing: 1px;
    color: var(--black);
    line-height: 1;
  }
  .strapline {
    position: absolute;
    left: 470px;
    top: 656px;
    width: 260px;
    text-align: center;
    font-family: "Montserrat", sans-serif;
    font-weight: 600;
    font-size: 11.5px;
    line-height: 15px;
    color: var(--white);
    text-transform: uppercase;
  }
  .quote-heading {
    position: absolute;
    right: 18px;
    top: 812px;
    margin: 0;
    font-family: "Didact Gothic", sans-serif;
    font-weight: 400;
    font-size: 32px;
    color: var(--white);
    white-space: nowrap;
  }
  .quote-heading .quote-word {
    font-size: 46px;
  }
  .panel-label {
    position: absolute;
    top: 920px;
    margin: 0;
    font-family: "Didact Gothic", sans-serif;
    font-weight: 400;
    font-size: 23px;
    color: var(--white);
    text-align: center;
  }
  .panel-label.for { left: 26px; width: 356px; }
  .panel-label.by { left: 474px; width: 348px; }
</style>
</head>
<body>
<main class="cover">
  <svg class="cover-shapes" width="849" height="1200" viewBox="0 0 849 1200" xmlns="http://www.w3.org/2000/svg">
    <defs>
      <linearGradient id="tech-glow" x1="0" y1="1" x2="1" y2="0">
        <stop offset="0" stop-color="#ffffff" stop-opacity="0"/>
        <stop offset="0.35" stop-color="var(--blue-soft)"/>
        <stop offset="1" stop-color="var(--blue-deep)"/>
      </linearGradient>
    </defs>

    <!-- header band -->
    <rect class="header-band" x="0" y="111" width="849" height="114" fill="var(--grey-light)"/>

    <!-- technology backdrop -->
    <polygon role="img" aria-label="Abstract blue technology panels with light lines"
             points="849,0 849,615 200,615 200,455 0,535 0,480"
             fill="url(#tech-glow)"/>

    <!-- strapline band -->
    <rect class="strap-band" x="200" y="641" width="649" height="93" fill="var(--grey-light)"/>
    <polygon points="480,627 496,627 404,734 388,734" fill="var(--black)"/>
    <polygon points="754,627 770,627 712,734 696,734" fill="var(--black)"/>
    <polygon class="strap-tab" points="492,627 758,627 700,734 418,734" fill="var(--orange)"/>

    <!-- quote band -->
    <polygon class="quote-band" points="193,753 849,753 849,877 0,877" fill="var(--orange-band)"/>

    <!-- prepared panels -->
    <polygon class="panel-for" points="0,905 428,905 402,1104 0,1104" fill="var(--grey-panel)"/>
    <polygon class="panel-by" points="455,905 849,905 849,1104 416,1104" fill="var(--grey-panel)"/>
    <rect x="26" y="960" width="356" height="4" fill="var(--white)"/>
    <rect x="474" y="960" width="348" height="4" fill="var(--white)"/>

    <!-- footer band -->
    <rect class="footer-band" x="0" y="1140" width="849" height="60" fill="var(--grey-light)"/>
  </svg>

  <div class="brand">
    <span class="brand-dot"></span>
    <span class="brand-name">QUILLBARROW</span>
  </div>

  <p class="strapline">Bringing enterprise-level<br>IT solutions to<br>East Anglia businesses</p>

  <h1 class="quote-heading">We Have Prepared a <span class="quote-word">Quote</span> For You</h1>

  <p class="panel-label for">Prepared for</p>
  <p class="panel-label by">Prepared by</p>
</main>
</body>
</html>
```